Business card required for IT Consultancy Business - Tealbrook Consulting.
Company provides the whole nine yards of services across IT Architecture, design and execution.
Basically we provide consulting services to help businesses make sure their technology is enabling their business strategy.
Design for front and back required.
We would like the front of the card to inlcude:
Name
Title
Mobile number
email address
www.tbkc.com.au
Company logos attached.
Thank you
Industry/Entity Type
Business
Contact Information for Business Card
Name
Title
Mobile number
email address
www.tbkc.com.au
Look and feel
Each slider illustrates characteristics of the customer's brand and the style your logo design should communicate.

```html
<!DOCTYPE html>
<html lang="en">
<head>
<meta charset="utf-8">
<title>Tealbrook Consulting – Business Card</title>
<link href="https://fonts.googleapis.com/css2?family=Roboto:ital,wght@0,400;0,500;0,700;1,700&display=swap" rel="stylesheet">
<style>
  :root {
    --brand-blue: #1877c6;
    --brand-blue-deep: #1266b0;
    --brand-orange: #f0592a;
    --paper: #ffffff;
    --ink: #1c1c1c;
    --backdrop: #6c7378;
  }
  * { box-sizing: border-box; margin: 0; padding: 0; }
  html, body {
    width: 1200px; height: 900px; overflow: hidden;
    background: var(--backdrop);
    font-family: "Roboto", Arial, sans-serif;
  }
  .canvas {
    position: relative; width: 1200px; height: 900px;
  }
  .card {
    position: absolute; left: 320px; width: 560px; height: 320px;
    overflow: hidden;
    box-shadow: 0 10px 24px rgba(0,0,0,.35);
  }
  .card--back { top: 80px; background: var(--brand-blue); }
  .card--front { top: 480px; background: var(--paper); }

  /* back side */
  .back-logo {
    position: absolute; left: 0; right: 0; top: 120px;
    display: flex; align-items: center; justify-content: center; gap: 14px;
  }
  .logo-dot {
    width: 34px; height: 34px; border-radius: 50%;
    background: var(--brand-orange);
  }
  .back-logo .logo-name {
    color: var(--paper); font-weight: 700; font-size: 40px; letter-spacing: .5px;
  }
  .back-url {
    position: absolute; left: 60px; bottom: 40px;
    color: var(--paper); font-size: 14px;
  }

  /* front side */
  .wave { position: absolute; inset: 0; }
  .front-logo {
    position: absolute; left: 32px; top: 30px;
    display: flex; align-items: center; gap: 10px;
  }
  .front-logo .logo-dot { width: 24px; height: 24px; }
  .front-logo .logo-name {
    color: var(--brand-blue); font-weight: 700; font-size: 26px;
  }
  .person {
    position: absolute; right: 40px; top: 140px; text-align: right;
  }
  .person-name {
    color: var(--brand-blue); font-weight: 700; font-style: italic;
    font-size: 24px; letter-spacing: .5px;
  }
  .person-title {
    color: var(--ink); font-size: 10px; font-weight: 500; letter-spacing: .5px;
  }
  .contact {
    position: absolute; right: 120px; top: 236px;
    list-style: none; color: var(--paper); font-size: 14px; line-height: 20px;
  }
  .contact li {
    display: flex; justify-content: flex-end; align-items: center; gap: 8px;
  }
  .contact svg { width: 12px; height: 12px; flex: none; }
</style>
</head>
<body>
<main class="canvas">

  <section class="card card--back" aria-label="Card back">
    <div class="back-logo">
      <span class="logo-dot"></span>
      <span class="logo-name">Tealbrook Consulting</span>
    </div>
    <p class="back-url">www.tbkc.com.au</p>
  </section>

  <section class="card card--front" aria-label="Card front">
    <svg class="wave" viewBox="0 0 560 320" aria-hidden="true">
      <path d="M0,115 C150,170 250,215 380,225 C470,232 530,260 560,290 L560,320 L0,320 Z" fill="var(--brand-blue)"/>
      <path d="M0,108 C150,163 250,208 380,218 C470,225 530,253 560,283" fill="none" stroke="var(--brand-orange)" stroke-width="2"/>
      <path d="M0,128 C70,160 130,190 210,210" fill="none" stroke="var(--paper)" stroke-width="4" stroke-linecap="round"/>
      <path d="M0,140 C90,190 180,230 300,245 C420,258 500,275 540,300" fill="none" stroke="var(--brand-blue-deep)" stroke-width="6" opacity=".6"/>
    </svg>

    <div class="front-logo">
      <span class="logo-dot"></span>
      <span class="logo-name">Tealbrook Consulting</span>
    </div>

    <div class="person">
      <p class="person-name">JOHN DOE</p>
      <p class="person-title">OWNER</p>
    </div>

    <ul class="contact">
      <li>123-456-1234
        <svg viewBox="0 0 12 12"><path d="M3 1 L5 3.5 L4 5 C4.6 6.4 5.6 7.4 7 8 L8.5 7 L11 9 L10 11 C5 11 1 7 1 2 Z" fill="currentColor"/></svg>
      </li>
      <li>123-123-1234
        <svg viewBox="0 0 12 12"><rect x="3" y="0.5" width="6" height="11" rx="1" fill="none" stroke="currentColor"/><circle cx="6" cy="9.5" r=".7" fill="currentColor"/></svg>
      </li>
      <li>yourmail@email.com
        <svg viewBox="0 0 12 12"><rect x="0.5" y="2.5" width="11" height="7" fill="none" stroke="currentColor"/><path d="M0.5 2.5 L6 7 L11.5 2.5" fill="none" stroke="currentColor"/></svg>
      </li>
      <li>www.tbkc.com.au
        <svg viewBox="0 0 12 12"><circle cx="6" cy="6" r="5" fill="none" stroke="currentColor"/><path d="M1 6 H11 M6 1 C3.5 4 3.5 8 6 11 C8.5 8 8.5 4 6 1" fill="none" stroke="currentColor" stroke-width=".8"/></svg>
      </li>
    </ul>
  </section>

</main>
</body>
</html>
```